The most modern business card ever !!!

Our company call “Tavlin”. Tavlin is a technology company specialized in cruises solutions. Out main product is a platform to reserve cruises. This is a revolutionary platform that make easier to travel agencies and final users to reserve cruises across dozen companies like brindle, pelvo, tkw, vbd, etc..We are a “start up”, with a young team of developers and we want to transmit it.. For it, we want something different, a modern business card that represent cruises and technology.. When someone receive this card, this person should say: wowww this is different… this is modern… this is a cruise related company..
Contact Information for Business Card
Requirements
Must have
- diferent, modern
Should not have
- traditions business card

```html
<!DOCTYPE html>
<html lang="en">
<head>
<meta charset="utf-8">
<title>Tavlin — Business Card</title>
<link href="https://fonts.googleapis.com/css2?family=Roboto:wght@400;500;700;900&display=swap" rel="stylesheet">
<style>
  :root{
    --stage:#7a7a7a;
    --card-grey:#5f5f60;
    --band-dark:#262627;
    --band-edge:#9a9a9a;
    --photo-warm:#cdbba2;
    --photo-cool:#d9dde1;
    --photo-deep:#8d7a66;
    --ink:#111111;
    --accent:#1aa0e0;
    --paper:#f4f4f4;
  }
  *{box-sizing:border-box;margin:0;padding:0}
  html,body{width:1200px;height:900px;overflow:hidden}
  body{background:var(--stage);font-family:"Roboto",sans-serif;position:relative}
  .card{position:absolute;top:296px;width:540px;height:309px;overflow:hidden;
        background:var(--card-grey);box-shadow:0 14px 30px rgba(0,0,0,.35)}
  .card--front{left:40px}
  .card--back{left:620px}
  .photo{position:absolute;inset:0;
         background:
          radial-gradient(ellipse at 40% 40%, var(--photo-cool) 0%, transparent 55%),
          linear-gradient(125deg, var(--photo-warm) 0%, var(--photo-deep) 55%, var(--photo-warm) 100%)}
  .card--front .photo{-webkit-mask:linear-gradient(180deg,#000 0%,#000 45%,transparent 72%);
                      mask:linear-gradient(180deg,#000 0%,#000 45%,transparent 72%)}
  .card--back .photo{-webkit-mask:linear-gradient(0deg,#000 0%,#000 50%,transparent 72%);
                     mask:linear-gradient(0deg,#000 0%,#000 50%,transparent 72%)}
  .wash{position:absolute;inset:0}
  .card--front .wash{background:linear-gradient(180deg,rgba(255,255,255,.25) 0%,rgba(255,255,255,.45) 35%,transparent 60%)}
  .card--back .wash{background:linear-gradient(0deg,rgba(255,255,255,.45) 0%,rgba(255,255,255,.6) 45%,transparent 68%)}
  .geometry{position:absolute;left:0;width:540px;height:309px}
  .brand{position:absolute;left:120px;top:56px;font-weight:700;font-size:62px;
         letter-spacing:4px;color:var(--ink)}
  .identity{position:absolute;left:250px;top:160px}
  .identity__name{font-weight:700;font-size:24px;color:var(--ink);letter-spacing:.3px}
  .identity__role{font-weight:400;font-size:15px;color:var(--accent);margin-top:1px}
  .contacts{position:absolute;left:170px;top:218px;display:flex;gap:14px}
  .contacts__icons{border:2.5px solid var(--ink);border-radius:5px;padding:5px 7px;
                   display:flex;flex-direction:column;gap:5px;background:rgba(255,255,255,.35)}
  .contacts__icons svg{width:13px;height:13px;display:block;fill:var(--accent)}
  .contacts__list{list-style:none;display:flex;flex-direction:column;gap:3px;
                  font-size:13px;font-weight:500;color:var(--ink);line-height:15px;padding-top:3px}
</style>
</head>
<body>

<section class="card card--front" aria-label="Card front">
  <div class="photo" role="img" aria-label="Photograph of a team bumping fists over a desk with laptops and phones"></div>
  <div class="wash"></div>
  <svg class="geometry" viewBox="0 0 540 309" aria-hidden="true">
    <polygon points="0,190 540,175 540,188 0,203" fill="var(--band-dark)"/>
    <polygon points="300,309 330,120 344,120 314,309" fill="var(--band-dark)"/>
    <polygon points="430,309 400,80 414,80 444,309" fill="var(--band-dark)"/>
    <polygon points="120,309 540,250 540,262 120,309" fill="var(--band-dark)"/>
    <line x1="344" y1="120" x2="314" y2="309" stroke="var(--band-edge)" stroke-width="1.5"/>
    <line x1="414" y1="80" x2="444" y2="309" stroke="var(--band-edge)" stroke-width="1.5"/>
  </svg>
  <div class="brand">Tavlin</div>
</section>

<section class="card card--back" aria-label="Card back">
  <div class="photo" role="img" aria-label="Photograph of a team bumping fists over a desk with laptops and phones"></div>
  <div class="wash"></div>
  <svg class="geometry" viewBox="0 0 540 309" aria-hidden="true">
    <polygon points="0,40 540,30 540,42 0,52" fill="var(--band-dark)"/>
    <polygon points="0,112 540,100 540,112 0,124" fill="var(--band-dark)"/>
    <polygon points="120,0 105,150 118,150 133,0" fill="var(--band-dark)"/>
    <polygon points="240,0 200,170 214,170 254,0" fill="var(--band-dark)"/>
    <polygon points="40,0 20,120 32,120 52,0" fill="var(--band-dark)"/>
    <line x1="133" y1="0" x2="118" y2="150" stroke="var(--band-edge)" stroke-width="1.5"/>
    <line x1="254" y1="0" x2="214" y2="170" stroke="var(--band-edge)" stroke-width="1.5"/>
  </svg>
  <div class="identity">
    <div class="identity__name">Marlo Venrick</div>
    <div class="identity__role">Managing Director</div>
  </div>
  <div class="contacts">
    <div class="contacts__icons">
      <svg viewBox="0 0 24 24"><path d="M6.6 10.8a15.1 15.1 0 0 0 6.6 6.6l2.2-2.2a1 1 0 0 1 1-.25 11.4 11.4 0 0 0 3.6.57 1 1 0 0 1 1 1V20a1 1 0 0 1-1 1A17 17 0 0 1 3 4a1 1 0 0 1 1-1h3.5a1 1 0 0 1 1 1c0 1.25.2 2.45.57 3.57a1 1 0 0 1-.25 1z"/></svg>
      <svg viewBox="0 0 24 24"><path d="M2 5h20v14H2z M2 5l10 8 10-8" stroke="#fff" stroke-width="1.5"/></svg>
      <svg viewBox="0 0 24 24"><circle cx="12" cy="12" r="10"/><path d="M2 12h20M12 2c3 3 3 17 0 20M12 2c-3 3-3 17 0 20" stroke="#fff" stroke-width="1.3" fill="none"/></svg>
      <svg viewBox="0 0 24 24"><path d="M12 2a7 7 0 0 0-7 7c0 5 7 13 7 13s7-8 7-13a7 7 0 0 0-7-7zm0 9.5A2.5 2.5 0 1 1 12 6.5a2.5 2.5 0 0 1 0 5z"/></svg>
    </div>
    <ul class="contacts__list">
      <li>(014)2781.365</li>
      <li>hello@tavlinmail.com</li>
      <li>www.tavlinweb.com</li>
      <li>2284 Harlow Quay Drive,USA</li>
    </ul>
  </div>
</section>

</body>
</html>
```